Real Estate Sign Project

We need a Real Estate sign that promotes the property being listed and our company and agent listing the property. The images need to be able to be swapped out so we can use the template for each listing we have. I have a sample from another company that shows what were are trying to accomplish. Would want ours to be unique using our logo and the colors in our logo. We would like to not have to use a rider. Would want agents name and phone number to be part of the 36" x 24" sign.

Industry/Entity Type

Real Estate

Requirements
Must have
• Sign dimensions are 36 inches by 24 inches (36" across and 24" up down). Use example.of.sign.we.want.jpg as the direction we want to go but with a different layout and our logo and colors. This would be just a template that we can swap out new pictures, address, price, website, agents contact info for each home we are listing. Like the idea of the pictures bleeding off the sides. Please use free stock photos for the home images as we will be changing these out for each listing. Please incorporate all info including agents info into the one sign. File must be layered so we can change the pictures, price, website, agent, etc. We use GIMP (.xcf) file

```html
<!DOCTYPE html>
<html lang="en">
<head>
<meta charset="utf-8">
<title>Home For Sale – 1846 Larkspur Road</title>
<link href="https://fonts.googleapis.com/css2?family=Source+Sans+3:wght@400;600;700&display=swap" rel="stylesheet">
<style>
  :root {
    --orange: #e2621f;
    --navy: #1c2b4b;
    --blue: #1f7cc2;
    --sky: #3a95dc;
    --ink: #24346a;
    --white: #ffffff;
  }
  * { box-sizing: border-box; margin: 0; padding: 0; }
  html, body { width: 1200px; height: 801px; overflow: hidden; background: var(--white); }
  body { font-family: "Source Sans 3", Arial, sans-serif; }
  .sign { position: relative; width: 1200px; height: 801px; background: var(--orange); overflow: hidden; }

  .brand-box { position: absolute; left: 0; top: 0; width: 442px; height: 146px; background: var(--white);
    display: flex; align-items: center; gap: 16px; padding-left: 36px; }
  .brand-square { width: 46px; height: 46px; background: var(--blue); flex: none; }
  .brand-name { color: var(--ink); font-weight: 700; font-size: 30px; line-height: 1; }

  .headline { position: absolute; left: 442px; top: 0; right: 0; height: 146px; display: flex;
    align-items: center; justify-content: flex-end; gap: 26px; padding-right: 26px; color: var(--white); }
  .headline-label { font-size: 36px; font-weight: 400; margin-top: 14px; }
  .headline-price { font-size: 88px; font-weight: 700; letter-spacing: -1px; }

  .photo { position: absolute; }
  .photo-bath { left: 0; top: 146px; width: 434px; height: 313px; background: linear-gradient(135deg, #f1eee9, #cfc8bd 60%, #8c6a4e); }
  .photo-bedroom { left: 440px; top: 146px; width: 482px; height: 313px; background: radial-gradient(ellipse at 50% 60%, #9c8c7a, #4a3a33 75%); }
  .photo-living { left: 929px; top: 146px; width: 271px; height: 147px; background: linear-gradient(135deg, #e3cfb2, #a56a3c 55%, #5a3420); }
  .photo-kitchen { left: 929px; top: 300px; width: 271px; height: 182px; background: linear-gradient(160deg, #ead9b8, #b99462 55%, #6e5233); }
  .photo-house { left: 929px; top: 489px; width: 271px; height: 122px; background: linear-gradient(180deg, #8fb9e0 0%, #d7dde2 45%, #9aa4a8 70%, #5f8a3a 100%); }

  .details { position: absolute; left: 0; top: 459px; width: 922px; height: 201px; background: var(--white);
    display: flex; align-items: center; color: var(--ink); }
  .address { font-size: 42px; font-weight: 400; padding-left: 60px; width: 460px; }
  .brace { width: 40px; height: 176px; flex: none; }
  .features { list-style: none; font-size: 30px; line-height: 39px; padding-left: 8px; }

  .web-band { position: absolute; left: 0; top: 660px; width: 1200px; height: 34px; background: var(--blue);
    color: var(--white); font-size: 22px; text-align: center; line-height: 34px; }

  .agent-band { position: absolute; left: 0; top: 694px; width: 1200px; height: 107px; background: var(--navy);
    display: flex; align-items: center; padding: 0 32px; color: var(--white); }
  .agent-mark { width: 64px; height: 64px; border-radius: 50%; background: var(--orange); flex: none; margin-right: 24px; }
  .agent-name { font-size: 40px; font-weight: 700; }
  .agent-label { color: var(--sky); margin-right: 10px; }
  .agent-phone { margin-left: auto; font-size: 42px; font-weight: 700; padding-right: 18px; }
</style>
</head>
<body>
<div class="sign">
  <header class="brand-box">
    <span class="brand-square"></span>
    <span class="brand-name">Kestrel Home Group</span>
  </header>
  <div class="headline">
    <span class="headline-label">Home For Sale</span>
    <span class="headline-price">$360,000</span>
  </div>

  <div class="photo photo-bath" role="img" aria-label="Listing photo: bathroom with glass shower"></div>
  <div class="photo photo-bedroom" role="img" aria-label="Listing photo: master bedroom"></div>
  <div class="photo photo-living" role="img" aria-label="Listing photo: living room with fireplace"></div>
  <div class="photo photo-kitchen" role="img" aria-label="Listing photo: kitchen with granite island"></div>
  <div class="photo photo-house" role="img" aria-label="Listing photo: front exterior of the home"></div>

  <section class="details">
    <div class="address">1846 Larkspur Road</div>
    <svg class="brace" viewBox="0 0 40 176" aria-hidden="true">
      <path d="M34 4 C18 4 20 14 20 30 L20 72 C20 82 14 88 4 88 C14 88 20 94 20 104 L20 146 C20 162 18 172 34 172"
            fill="none" stroke="#24346a" stroke-width="3"/>
    </svg>
    <ul class="features">
      <li>4 Bedrooms</li>
      <li>3.5 Baths</li>
      <li>3200 Finished SF</li>
      <li>2-Car Garage</li>
    </ul>
  </section>

  <div class="web-band">KestrelHomeGroup.com/1846Larkspur</div>

  <footer class="agent-band">
    <span class="agent-mark"></span>
    <span class="agent-name"><span class="agent-label">AGENT:</span>John Doe</span>
    <span class="agent-phone">xxx/xxx/xxxx</span>
  </footer>
</div>
</body>
</html>
```